New Year Resolution Infographic

We are a weight loss company that provides holistic, natural nutrition programs to consumers -- you can see our Web site at www.SlimBirch.com We need a simple infographic to be shared on social media and via email for New Year's day. The topic for the infographic is "how to set and keep your weight loss resolution". We've outlined 5 process steps for consumers to follow to assist with their weight loss resolutions, and we would like to depict this graphically.

Target Market(s)

Women age 35-65 who are planning to make a resolution to lose weight in the new year.

Industry/Entity Type

Health And Wellness

Font styles to use
Sans Serif

Colors
0392cd
9bcb3c

Requirements
Must have
• Initial graphic showing failure stats (see copy)
• Graphic showing process steps in making/keeping a resolution (see copy)
• SlimBirch Logo

```html
<!DOCTYPE html>
<html lang="en">
<head>
<meta charset="utf-8">
<title>SlimBirch – New Year Resolution Guide</title>
<link href="https://fonts.googleapis.com/css2?family=Montserrat:wght@400;500;700;800&family=Nunito:wght@900&display=swap" rel="stylesheet">
<style>
:root{
  --blue:#0392cd;
  --green:#9bcb3c;
  --ink:#2b2b2b;
  --grey:#c4c5c7;
  --stage:#d1d2d4;
  --white:#ffffff;
}
*{margin:0;padding:0;box-sizing:border-box}
html,body{width:1200px;height:1200px;overflow:hidden;background:var(--stage)}
body{font-family:"Montserrat",sans-serif;color:var(--ink);position:relative}
.poster{position:absolute;left:277.6px;top:69.6px;width:805px;height:1326px;background:var(--white);transform:scale(.8);transform-origin:0 0;overflow:hidden}
.abs{position:absolute}
.brand-block{left:0;top:40px;width:38px;height:48px;background:var(--blue)}
.brand-name{left:52px;top:36px;font-size:50px;font-weight:700;color:var(--blue);letter-spacing:-1px;line-height:56px}
.url-ribbon{left:462px;top:40px}
.url-text{left:462px;top:40px;width:250px;height:48px;line-height:48px;text-align:center;color:var(--white);font-size:18px;font-weight:500;letter-spacing:.3px}
.headline{left:51px;top:132px;font-size:36px;font-weight:500;color:var(--ink);letter-spacing:.5px}
.headline b{color:var(--blue);font-weight:700}
.banner{left:12px;top:182px}
.banner-text{left:52px;top:180px;font-family:"Nunito",sans-serif;font-weight:900;font-size:47px;color:var(--white);line-height:60px;letter-spacing:.5px}
.hero-badge{left:622px;top:132px;width:146px;height:146px;border:4px solid var(--green);border-radius:50%;background:var(--white);display:flex;align-items:center;justify-content:center}
.hero-art{width:104px;height:104px;border-radius:50%;background:linear-gradient(160deg,#e3eef5,#b9c7cf)}
.intro{left:50px;top:256px;font-size:17px;line-height:22px;color:#4a4a4a;letter-spacing:.2px}
.g{color:var(--green);font-weight:700}
.bl{color:var(--blue);font-weight:500}
.blb{color:var(--blue);font-weight:700}
.stat-chart{left:150px;top:322px}
.stat-art{left:188px;top:360px;width:82px;height:84px;border-radius:50%;background:linear-gradient(160deg,#dceaf3,#9fb6c4)}
.stat-text{left:335px;top:352px;font-size:18px;line-height:22px;color:var(--ink);letter-spacing:.2px}
.guide-icon{left:47px;top:487px}
.guide-text{left:146px;top:504px;font-size:18px;line-height:22px;color:var(--ink);letter-spacing:.2px}
.guide-rule{left:47px;top:563px;width:600px;height:3px;background:var(--green)}
.guide-dot{left:640px;top:558px;width:13px;height:13px;border-radius:50%;background:var(--green)}
.step-icon{left:36px}
.step{left:223px;width:500px;font-size:15.5px;line-height:19px;color:var(--ink);letter-spacing:.15px}
.step-title{font-size:17.5px;font-weight:800;color:var(--blue);letter-spacing:.3px}
.step-rule{left:220px}
.footer{left:0;top:1110px}
.footer-text{left:48px;top:1186px;color:var(--white);font-size:18px;line-height:22px;letter-spacing:.3px}
.footer-text p+p{margin-top:13px}
.footer-text strong{font-weight:800}
</style>
</head>
<body>
<main class="poster">
  <header>
    <div class="abs brand-block"></div>
    <div class="abs brand-name">SlimBirch</div>
    <svg class="abs url-ribbon" width="300" height="48" viewBox="0 0 300 48"><polygon points="0,0 296,0 262,24 296,48 0,48" fill="var(--blue)"/></svg>
    <div class="abs url-text">www.SlimBirch.com</div>
  </header>

  <h1 class="abs headline">How to <b>SET</b> and <b>REACH</b> Your</h1>
  <svg class="abs banner" width="640" height="58" viewBox="0 0 640 58"><polygon points="0,0 640,0 640,58 0,58 36,29" fill="var(--green)"/></svg>
  <div class="abs banner-text">Weight Loss Resolution</div>
  <div class="abs hero-badge"><div class="hero-art" role="img" aria-label="Illustration of a person walking on a treadmill"></div></div>

  <p class="abs intro"><span class="g">WEIGHT LOSS</span> is the <span class="bl">#1 New Year</span> resolution, but we know<br>that <span class="g">RESOLUTIONS</span> are very difficult to keep.</p>

  <svg class="abs stat-chart" width="260" height="160" viewBox="0 0 260 160">
    <circle cx="78" cy="80" r="68" fill="none" stroke="var(--grey)" stroke-width="9"/>
    <path d="M142,58 A68,68 0 0 1 122,132" fill="none" stroke="var(--blue)" stroke-width="9"/>
    <polyline points="85,12 254,12 254,27" fill="none" stroke="#555" stroke-width="1.2"/>
    <circle cx="85" cy="12" r="2.5" fill="var(--white)" stroke="#555"/>
    <line x1="146" y1="86" x2="180" y2="86" stroke="#555" stroke-width="1.2"/>
    <circle cx="146" cy="86" r="2.5" fill="var(--white)" stroke="#555"/>
  </svg>
  <div class="abs stat-art" role="img" aria-label="Illustration of a runner on a treadmill"></div>
  <p class="abs stat-text">While <span class="blb">45% OF AMERICANS</span> make<br>New Year <span class="g">RESOLUTIONS</span>, only<br><span class="blb">8% SUCCEED</span> in keeping<br>those resolutions.</p>

  <svg class="abs guide-icon" width="74" height="78" viewBox="0 0 74 78" role="img" aria-label="Guide book with magnifier">
    <path d="M2,76 V6 Q2,2 6,2 H64 V8" fill="none" stroke="var(--green)" stroke-width="3"/>
    <rect x="12" y="8" width="58" height="68" fill="none" stroke="var(--green)" stroke-width="3"/>
    <circle cx="36" cy="36" r="13" fill="none" stroke="var(--blue)" stroke-width="3"/>
    <line x1="45" y1="46" x2="58" y2="60" stroke="var(--blue)" stroke-width="5" stroke-linecap="round"/>
  </svg>
  <p class="abs guide-text">Here is a <span class="blb">QUICK GUIDE</span> to setting and reaching your<br><span class="g">WEIGHT LOSS</span> resolution this year.</p>
  <div class="abs guide-rule"></div>
  <div class="abs guide-dot"></div>

  <svg class="abs step-icon" style="top:595px" width="150" height="80" viewBox="0 0 150 80" role="img" aria-label="Bathroom scale icon"><path d="M14,66 A61,61 0 0 1 136,66" fill="var(--white)" stroke="var(--blue)" stroke-width="6"/><line x1="0" y1="67" x2="150" y2="67" stroke="#8d8e90" stroke-width="2"/><polygon points="68,68 82,68 75,75" fill="#8d8e90"/><circle cx="75" cy="40" r="22" fill="#d6d8da"/></svg>
  <div class="abs step" style="top:606px"><strong class="step-title">REFLECT:</strong> Get clear on why the achievement of your resolution is important. You'll need to come back to this if you falter!</div>
  <svg class="abs step-rule" style="top:682px" width="516" height="14" viewBox="0 0 516 14"><circle cx="6" cy="7" r="4.5" fill="var(--white)" stroke="var(--blue)" stroke-width="1.5"/><line x1="14" y1="7" x2="506" y2="7" stroke="var(--blue)" stroke-width="2" stroke-dasharray="2 3"/><circle cx="509" cy="7" r="5" fill="var(--blue)"/></svg>

  <svg class="abs step-icon" style="top:700px" width="150" height="80" viewBox="0 0 150 80" role="img" aria-label="Meal plan clipboard and dumbbell icon"><path d="M14,66 A61,61 0 0 1 136,66" fill="var(--white)" stroke="var(--blue)" stroke-width="6"/><line x1="0" y1="67" x2="150" y2="67" stroke="#8d8e90" stroke-width="2"/><polygon points="68,68 82,68 75,75" fill="#8d8e90"/><circle cx="75" cy="40" r="22" fill="#d6d8da"/></svg>
  <div class="abs step" style="top:711px"><strong class="step-title">RESOLVE:</strong> Set a weight loss goal for the year that is realistic, then break this up into even shorter term goals of 30-60 days, with a specific diet and activity plan to guide you.</div>
  <svg class="abs step-rule" style="top:787px" width="516" height="14" viewBox="0 0 516 14"><circle cx="6" cy="7" r="4.5" fill="var(--white)" stroke="var(--blue)" stroke-width="1.5"/><line x1="14" y1="7" x2="506" y2="7" stroke="var(--blue)" stroke-width="2" stroke-dasharray="2 3"/><circle cx="509" cy="7" r="5" fill="var(--blue)"/></svg>

  <svg class="abs step-icon" style="top:804px" width="150" height="80" viewBox="0 0 150 80" role="img" aria-label="Healthy food icon"><path d="M14,66 A61,61 0 0 1 136,66" fill="var(--white)" stroke="var(--blue)" stroke-width="6"/><line x1="0" y1="67" x2="150" y2="67" stroke="#8d8e90" stroke-width="2"/><polygon points="68,68 82,68 75,75" fill="#8d8e90"/><circle cx="75" cy="40" r="22" fill="#d6d8da"/></svg>
  <div class="abs step" style="top:816px"><strong class="step-title">REPLACE:</strong> Clear out your pantry and stock up with only healthy foods. Then work to build new activity and eating habits that take the place of your current habits.</div>
  <svg class="abs step-rule" style="top:891px" width="516" height="14" viewBox="0 0 516 14"><circle cx="6" cy="7" r="4.5" fill="var(--white)" stroke="var(--blue)" stroke-width="1.5"/><line x1="14" y1="7" x2="506" y2="7" stroke="var(--blue)" stroke-width="2" stroke-dasharray="2 3"/><circle cx="509" cy="7" r="5" fill="var(--blue)"/></svg>

  <svg class="abs step-icon" style="top:909px" width="150" height="80" viewBox="0 0 150 80" role="img" aria-label="Progress log document icon"><path d="M14,66 A61,61 0 0 1 136,66" fill="var(--white)" stroke="var(--blue)" stroke-width="6"/><line x1="0" y1="67" x2="150" y2="67" stroke="#8d8e90" stroke-width="2"/><polygon points="68,68 82,68 75,75" fill="#8d8e90"/><circle cx="75" cy="40" r="22" fill="#d6d8da"/></svg>
  <div class="abs step" style="top:921px"><strong class="step-title">RECORD:</strong> Track your progress daily, tell your family and friends about your resolution to create more accountability, and recruit a partner to share your journey.</div>
  <svg class="abs step-rule" style="top:996px" width="516" height="14" viewBox="0 0 516 14"><circle cx="6" cy="7" r="4.5" fill="var(--white)" stroke="var(--blue)" stroke-width="1.5"/><line x1="14" y1="7" x2="506" y2="7" stroke="var(--blue)" stroke-width="2" stroke-dasharray="2 3"/><circle cx="509" cy="7" r="5" fill="var(--blue)"/></svg>

  <svg class="abs step-icon" style="top:1014px" width="150" height="80" viewBox="0 0 150 80" role="img" aria-label="Apple with measuring tape icon"><path d="M14,66 A61,61 0 0 1 136,66" fill="var(--white)" stroke="var(--blue)" stroke-width="6"/><line x1="0" y1="67" x2="150" y2="67" stroke="#8d8e90" stroke-width="2"/><circle cx="75" cy="40" r="22" fill="#d6d8da"/></svg>
  <div class="abs step" style="top:1025px"><strong class="step-title">REWARD:</strong> Rather than using unhealthy food as a reward or cheat, give yourself healthy or relaxing experiences – such a spa treatment or taking a new fitness class.</div>
  <svg class="abs step-rule" style="top:1101px" width="516" height="14" viewBox="0 0 516 14"><circle cx="6" cy="7" r="4.5" fill="var(--white)" stroke="var(--blue)" stroke-width="1.5"/><line x1="14" y1="7" x2="506" y2="7" stroke="var(--blue)" stroke-width="2" stroke-dasharray="2 3"/><circle cx="509" cy="7" r="5" fill="var(--blue)"/></svg>

  <svg class="abs footer" width="805" height="216" viewBox="0 0 805 216">
    <defs><linearGradient id="swoosh" x1="0" x2="1"><stop offset="0" stop-color="#ffffff"/><stop offset="1" stop-color="#a9aaac"/></linearGradient></defs>
    <path d="M0,28 Q440,-10 805,206 L805,216 L0,216Z" fill="url(#swoosh)"/>
    <path d="M0,38 Q430,12 805,214 L805,216 L0,216Z" fill="var(--green)"/>
    <path d="M0,56 Q420,26 795,216 L0,216Z" fill="var(--blue)"/>
  </svg>
  <div class="abs footer-text">
    <p><strong>SlimBirch</strong> can help you achieve your<br><strong>WEIGHT LOSS RESOLUTION</strong> in the New Year.</p>
    <p>We invite you to learn more and<br>contact us for a <strong>FREE CONSULTATION</strong>.</p>
  </div>
</main>
</body>
</html>
```